Design A Dog Teeth Cleaning Certificate

Hello,
I need a Dog Teeth Cleaning Certificate made to fit on a standard tabvue display. I will provide exact dimensions at a later time. Now please design for tabvue.

Theme and artwork should match our brand and current logo. See attached word document for stashly link and further details.

Certificate would be given to all Pet Parents who have their pets teeth cleaned without Anesthesia as a certificate of completion.

I would like you to be creative and come up with something fun.

Examples: https://www.quorvel.example/find?q=Certificate+for+teeth+cleaning&client=brewsa-a&hs=K7T&rls=org.tandrix:en-US:official&source=lnms&tbm=isch&sa=X&ei=pq7LMrv2KacmzQJ3-TQNpd&ved=0DbKQ_BVoBQ&biw=1411&bih=718

Please allow a place for Pet Parent name and Pets name.

```html
<!DOCTYPE html>
<html lang="en">
<head>
<meta charset="utf-8">
<title>Dog Teeth Cleaning Certificate</title>
<link rel="stylesheet" href="https://fonts.googleapis.com/css2?family=Cinzel:wght@700&family=Lobster&family=Montserrat:wght@400;500;700&display=swap">
<style>
  :root {
    --gold-light: #f3dc8a;
    --gold: #c9a23e;
    --gold-dark: #7a5a14;
    --title-gold: #c8a450;
    --title-shadow: #6b4d12;
    --paper: #fbf6e6;
    --paper-deep: #f3ead0;
    --red: #c8191e;
    --ink: #141414;
    --ink-soft: #3a3a3a;
  }
  * { margin: 0; padding: 0; box-sizing: border-box; }
  html, body { width: 1200px; height: 856px; overflow: hidden; background: #ffffff; }

  .certificate {
    position: relative;
    width: 1200px;
    height: 856px;
    background: linear-gradient(135deg, var(--gold-dark) 0%, var(--gold-light) 22%, var(--gold) 45%, var(--gold-light) 65%, var(--gold-dark) 100%);
    font-family: "Montserrat", sans-serif;
    color: var(--ink);
  }
  .frame-inner {
    position: absolute;
    inset: 30px;
    border: 8px solid var(--gold-dark);
    background: linear-gradient(180deg, var(--gold-light), var(--gold));
  }
  .paper {
    position: absolute;
    inset: 46px;
    background: radial-gradient(ellipse at center, var(--paper) 55%, var(--paper-deep) 100%);
    box-shadow: inset 0 0 0 2px var(--gold-dark), inset 0 0 18px rgba(120, 90, 20, 0.35);
  }

  .title-block { font-size: inherit; }
  .title {
    position: absolute;
    left: 110px;
    width: 760px;
    text-align: center;
    white-space: nowrap;
    font-family: "Cinzel", serif;
    font-weight: 700;
    color: var(--title-gold);
    text-shadow: 2px 2px 0 var(--title-shadow);
    line-height: 1;
  }
  .title-line-1 { top: 108px; font-size: 54px; }
  .title-line-2 { top: 170px; font-size: 58px; }

  .title-rule { position: absolute; left: 207px; top: 240px; }

  .paw { position: absolute; width: 68px; height: 62px; border-radius: 50%; background: var(--title-gold); box-shadow: 2px 2px 0 var(--title-shadow); }
  .paw-left { left: 128px; top: 188px; }
  .paw-right { left: 786px; top: 188px; }

  .brand {
    position: absolute;
    left: 896px;
    top: 70px;
    width: 180px;
    display: flex;
    flex-direction: column;
    align-items: center;
    gap: 10px;
  }
  .brand-mark { width: 140px; height: 140px; border-radius: 50%; background: var(--red); }
  .brand-name { font-family: "Montserrat", sans-serif; font-weight: 700; font-size: 22px; color: var(--red); }

  .headline {
    position: absolute;
    left: 158px;
    top: 268px;
    font-family: "Lobster", cursive;
    font-size: 140px;
    line-height: 1;
    color: var(--red);
    letter-spacing: 1px;
    white-space: nowrap;
  }

  .statement {
    position: absolute;
    left: 164px;
    font-size: 34px;
    font-weight: 500;
    color: var(--ink);
    line-height: 1;
    white-space: nowrap;
  }
  .statement-name { top: 452px; display: flex; align-items: flex-end; }
  .statement-name .fill-line { display: inline-block; width: 530px; border-bottom: 2px solid var(--ink); margin-left: 14px; height: 30px; }
  .statement-clinic { top: 500px; }
  .clinic-title {
    position: absolute;
    left: 164px;
    top: 546px;
    font-size: 30px;
    font-weight: 700;
    letter-spacing: 6.5px;
    color: var(--title-gold);
    white-space: nowrap;
  }

  .seal { position: absolute; left: 162px; top: 605px; width: 190px; height: 130px; }
  .issue-date { position: absolute; left: 200px; top: 742px; font-size: 21px; color: var(--ink-soft); }

  .signature { position: absolute; top: 700px; text-align: center; font-size: 25px; color: var(--ink-soft); white-space: nowrap; }
  .signature::before { content: ""; display: block; border-top: 2px solid var(--ink); margin-bottom: 40px; }
  .signature-parents { left: 497px; width: 196px; }
  .signature-vet { left: 777px; width: 254px; }
</style>
</head>
<body>
<main class="certificate">
  <div class="frame-inner"></div>
  <div class="paper"></div>

  <span class="paw paw-left" role="img" aria-label="Gold paw print"></span>
  <span class="paw paw-right" role="img" aria-label="Gold paw print"></span>

  <h1 class="title-block">
    <span class="title title-line-1">DOG TEETH CLEANING</span>
    <span class="title title-line-2">CERTIFICATE</span>
  </h1>

  <svg class="title-rule" width="566" height="22" viewBox="0 0 566 22" aria-hidden="true">
    <path d="M0 11 L20 3 L546 3 L566 11 L546 19 L20 19 Z" fill="var(--title-shadow)"/>
    <path d="M4 11 L22 5 L544 5 L562 11 L544 16 L22 16 Z" fill="var(--title-gold)"/>
  </svg>

  <div class="brand">
    <span class="brand-mark" aria-hidden="true"></span>
    <span class="brand-name">Canine Gleam</span>
  </div>

  <p class="headline">Congratulation!</p>

  <p class="statement statement-name">Let it be know that <span class="fill-line"></span></p>
  <p class="statement statement-clinic">Has sucessfully participated to the clinic entitled</p>
  <p class="clinic-title">CLEANING TEETH WITHOUT ANESTHESIA</p>

  <svg class="seal" viewBox="0 0 190 130" aria-hidden="true">
    <path d="M8 82 L40 72 L40 108 L8 112 L22 96 Z" fill="var(--red)"/>
    <path d="M182 82 L150 72 L150 108 L182 112 L168 96 Z" fill="var(--red)"/>
    <circle cx="95" cy="62" r="60" fill="var(--gold)"/>
    <circle cx="95" cy="62" r="50" fill="var(--red)"/>
  </svg>
  <p class="issue-date">Jan - 2014</p>

  <p class="signature signature-parents">Pet’s parents</p>
  <p class="signature signature-vet">Veterinary Sergeon</p>
</main>
</body>
</html>
```